Coastline Haven Retreats Business Card Design

Design a business card for Coastline Haven Retreats. Look at the website for colors and reference. Card should have logo, name, title, office number, mobile number, email, URL and a tagline like, "Luxury Hotel & Resort Email Marketing" (This might change).

https://www.coastlinehavenretreats.example

The rest I will leave up to your imagination.

Contact Information for Business Card

Logo, name, title, office number, mobile number, email, URL and a tagline like, "Luxury Hotel & Resort Email Marketing" (This might change).

```html
<!DOCTYPE html>
<html lang="en">
<head>
<meta charset="utf-8">
<title>Coastline Haven Retreats – Business Card</title>
<link rel="stylesheet" href="https://fonts.googleapis.com/css2?family=Poppins:wght@400;500;600;700&display=swap">
<style>
  :root {
    --bg: #1f1f1f;
    --card-white: #ffffff;
    --brand-orange: #f57200;
    --ink: #111111;
    --rule: #8a8a8a;
    --on-orange: #ffffff;
  }
  * { box-sizing: border-box; margin: 0; padding: 0; }
  html, body {
    width: 1200px; height: 1108px; overflow: hidden;
    background: var(--bg);
    font-family: "Poppins", Arial, sans-serif;
  }
  .stage {
    position: relative; width: 1200px; height: 1108px;
    display: flex; align-items: center; justify-content: center; gap: 70px;
  }
  .card {
    position: relative; width: 400px; height: 680px;
    border-radius: 30px; overflow: hidden;
  }

  /* Front */
  .card-front { background: var(--card-white); }
  .brand-mark {
    position: absolute; top: 120px; left: 0; right: 0;
    display: flex; align-items: center; justify-content: center; gap: 12px;
  }
  .brand-mark__square {
    width: 22px; height: 22px; background: var(--brand-orange); flex: none;
  }
  .brand-mark__name {
    font-weight: 700; font-size: 25px; line-height: 1.1; color: var(--ink);
    text-transform: uppercase; letter-spacing: 0.5px;
  }
  .person {
    position: absolute; top: 345px; left: 0; right: 0; text-align: center;
  }
  .person__name {
    font-weight: 600; font-size: 30px; color: var(--ink); letter-spacing: 1px;
    text-transform: uppercase; line-height: 1.1;
  }
  .person__title {
    font-weight: 400; font-size: 19px; color: var(--brand-orange);
    text-transform: uppercase; letter-spacing: 0.5px; margin-top: 2px;
  }
  .icon-row {
    position: absolute; top: 438px; left: 40px; right: 40px;
    display: flex; align-items: center; gap: 8px;
  }
  .icon-row__rule { flex: 1; height: 1px; background: var(--rule); }
  .icon-row__badge {
    width: 32px; height: 32px; border-radius: 5px; background: var(--brand-orange);
    display: flex; align-items: center; justify-content: center;
  }
  .icon-row__badge svg { width: 18px; height: 18px; }
  .contact-list {
    position: absolute; top: 482px; left: 0; right: 0; text-align: center;
    list-style: none; color: var(--ink); font-size: 17px; line-height: 1.35;
  }
  .contact-list__url { font-size: 15.5px; }
  .tagline-band {
    position: absolute; left: 0; right: 0; bottom: 0; height: 86px;
    background: var(--brand-orange);
    display: flex; align-items: center; justify-content: center;
  }
  .tagline-band__text {
    color: var(--on-orange); font-weight: 500; font-size: 16.5px;
    text-transform: uppercase; letter-spacing: 0.3px;
  }

  /* Back */
  .card-back { background: var(--brand-orange); }
  .card-back__pattern {
    position: absolute; inset: 0;
    background: linear-gradient(160deg, #f77a0a 0%, #f27000 55%, #ec6a00 100%);
  }
  .card-back__brand {
    position: absolute; inset: 0;
    display: flex; align-items: center; justify-content: center; gap: 12px;
  }
  .card-back__square {
    width: 20px; height: 20px; background: var(--on-orange); flex: none;
  }
  .card-back__name {
    color: var(--on-orange); font-weight: 700; font-size: 23px;
    text-transform: uppercase; letter-spacing: 0.5px; line-height: 1.1;
  }
</style>
</head>
<body>
<main class="stage">

  <section class="card card-front" aria-label="Business card front">
    <div class="brand-mark">
      <span class="brand-mark__square"></span>
      <span class="brand-mark__name">Coastline Haven<br>Retreats</span>
    </div>

    <div class="person">
      <h1 class="person__name">Daniel Hartley</h1>
      <p class="person__title">Managing Director</p>
    </div>

    <div class="icon-row">
      <span class="icon-row__rule"></span>
      <span class="icon-row__badge" aria-label="Office phone">
        <svg viewBox="0 0 24 24" fill="none" stroke="#fff" stroke-width="2" stroke-linejoin="round"><path d="M3 9c0-3 4-5 9-5s9 2 9 5l-3 2-2-3H8l-2 3z"/><rect x="6" y="12" width="12" height="8" rx="1"/></svg>
      </span>
      <span class="icon-row__badge" aria-label="Mobile">
        <svg viewBox="0 0 24 24" fill="none" stroke="#fff" stroke-width="2"><rect x="7" y="2" width="10" height="20" rx="2"/><line x1="11" y1="18" x2="13" y2="18"/></svg>
      </span>
      <span class="icon-row__badge" aria-label="Email">
        <svg viewBox="0 0 24 24" fill="none" stroke="#fff" stroke-width="2" stroke-linejoin="round"><rect x="3" y="5" width="18" height="14"/><path d="M3 5l9 8 9-8"/></svg>
      </span>
      <span class="icon-row__badge" aria-label="Website">
        <svg viewBox="0 0 24 24" fill="none" stroke="#fff" stroke-width="2"><circle cx="12" cy="12" r="9"/><path d="M3 12h18M12 3c3 3 3 15 0 18M12 3c-3 3-3 15 0 18"/></svg>
      </span>
      <span class="icon-row__rule"></span>
    </div>

    <ul class="contact-list">
      <li>044-555 210 384</li>
      <li>044-555 210 384</li>
      <li>info@coastlinehavenretreats.example</li>
      <li class="contact-list__url">www.coastlinehavenretreats.example</li>
    </ul>

    <div class="tagline-band">
      <p class="tagline-band__text">Luxury Hotel &amp; Resort Email Marketing</p>
    </div>
  </section>

  <section class="card card-back" aria-label="Business card back">
    <div class="card-back__pattern" role="img" aria-label="Tone-on-tone repeating company name pattern"></div>
    <div class="card-back__brand">
      <span class="card-back__square"></span>
      <span class="card-back__name">Coastline Haven<br>Retreats</span>
    </div>
  </section>

</main>
</body>
</html>
```